Business Card for Coral Reef Shore Dive Lodge
Kelumpang Beach Resort & Dive Tour Sdn. Bhd.
Bright & Fun-filled
Harudin Bin Sulaiman Taib
QRT Marketing & HR Manager
C27-4, Meranti Square, Jalan Tuaran
88450 Kota Kinabalu, SABAH Malaysia.
kelumpangresort@mailnest.example
572918-K (KPL/LN 4721)
logo vector

```html
<!DOCTYPE html>
<html lang="en">
<head>
<meta charset="utf-8">
<title>Kelumpang Beach Resort – Business Card</title>
<link rel="stylesheet" href="https://fonts.googleapis.com/css2?family=Cinzel:wght@400;600&family=Lato:wght@400;700&display=swap">
<style>
  :root {
    --page-bg: #e9e6e1;
    --card-black: #0d0b0a;
    --gold: #c79a63;
    --gold-light: #e0bd8c;
    --tan: #b98d62;
    --ivory: #f4f1ec;
    --text-light: #d9d4cc;
  }
  * { margin: 0; padding: 0; box-sizing: border-box; }
  html, body { width: 1200px; height: 629px; overflow: hidden; }
  body {
    background: var(--page-bg);
    display: flex;
    align-items: center;
    justify-content: center;
    font-family: "Lato", sans-serif;
  }
  .business-card {
    position: relative;
    width: 980px;
    height: 560px;
    background: var(--card-black);
    overflow: hidden;
    box-shadow: 0 10px 30px rgba(0,0,0,0.25);
  }
  .brand {
    position: absolute;
    top: 92px;
    left: 0;
    width: 100%;
    text-align: center;
  }
  .brand-name {
    font-family: "Cinzel", serif;
    font-weight: 400;
    font-size: 64px;
    letter-spacing: 14px;
    color: var(--gold);
  }
  .brand-tagline {
    margin-top: 6px;
    font-family: "Cinzel", serif;
    font-size: 15px;
    letter-spacing: 7px;
    color: var(--gold);
    text-transform: uppercase;
  }
  .holder {
    position: absolute;
    left: 70px;
    top: 300px;
    color: var(--text-light);
  }
  .holder-name {
    font-family: "Cinzel", serif;
    font-weight: 600;
    font-size: 21px;
    color: var(--gold);
    letter-spacing: 1px;
  }
  .holder-title {
    margin-top: 4px;
    font-size: 14px;
    letter-spacing: 1px;
    text-transform: uppercase;
  }
  .company-address {
    margin-top: 22px;
    font-size: 13px;
    line-height: 1.6;
    font-style: normal;
  }
  .company-address .company-name { color: var(--gold-light); font-weight: 700; }
  .contact-list {
    position: absolute;
    right: 70px;
    top: 292px;
    list-style: none;
    color: var(--text-light);
    font-size: 14px;
  }
  .contact-item {
    display: flex;
    align-items: center;
    gap: 12px;
    height: 29px;
  }
  .contact-icon {
    width: 22px;
    height: 22px;
    flex: none;
  }
  .card-wave {
    position: absolute;
    left: 0;
    bottom: 0;
    width: 100%;
    height: 110px;
  }
</style>
</head>
<body>
  <main class="business-card">
    <header class="brand">
      <div class="brand-name">KELUMPANG</div>
      <div class="brand-tagline">Beach Resort &amp; Dive Tour</div>
    </header>

    <section class="holder">
      <div class="holder-name">Harudin Bin Sulaiman Taib</div>
      <div class="holder-title">QRT Marketing &amp; HR Manager</div>
      <address class="company-address">
        <span class="company-name">Kelumpang Beach Resort &amp; Dive Tour Sdn. Bhd.</span><br>
        572918-K (KPL/LN 4721)<br>
        C27-4, Meranti Square, Jalan Tuaran<br>
        88450 Kota Kinabalu, SABAH Malaysia.
      </address>
    </section>

    <ul class="contact-list">
      <li class="contact-item">
        <svg class="contact-icon" viewBox="0 0 22 22"><circle cx="11" cy="11" r="11" fill="var(--gold)"/><path d="M7.5 6h2l1 2.5-1.3 1a6 6 0 0 0 3.3 3.3l1-1.3 2.5 1v2a1 1 0 0 1-1 1A8.5 8.5 0 0 1 6.5 7a1 1 0 0 1 1-1z" fill="var(--card-black)"/></svg>
        <span>+6088 214 376</span>
      </li>
      <li class="contact-item">
        <svg class="contact-icon" viewBox="0 0 22 22"><circle cx="11" cy="11" r="11" fill="var(--gold)"/><path d="M7.5 6h2l1 2.5-1.3 1a6 6 0 0 0 3.3 3.3l1-1.3 2.5 1v2a1 1 0 0 1-1 1A8.5 8.5 0 0 1 6.5 7a1 1 0 0 1 1-1z" fill="var(--card-black)"/></svg>
        <span>+6088 214 377</span>
      </li>
      <li class="contact-item">
        <svg class="contact-icon" viewBox="0 0 22 22"><circle cx="11" cy="11" r="11" fill="var(--gold)"/><rect x="6" y="9" width="10" height="6" rx="1" fill="var(--card-black)"/><rect x="8" y="6" width="6" height="3" fill="var(--card-black)"/></svg>
        <span>+6088 214 380</span>
      </li>
      <li class="contact-item">
        <svg class="contact-icon" viewBox="0 0 22 22"><circle cx="11" cy="11" r="11" fill="var(--gold)"/><rect x="8" y="5" width="6" height="12" rx="1.2" fill="var(--card-black)"/><circle cx="11" cy="15" r="0.8" fill="var(--gold)"/></svg>
        <span>+6013 552 9014</span>
      </li>
      <li class="contact-item">
        <svg class="contact-icon" viewBox="0 0 22 22"><circle cx="11" cy="11" r="11" fill="var(--gold)"/><rect x="5.5" y="7" width="11" height="8" rx="1" fill="var(--card-black)"/><path d="M5.8 7.5 11 11.5l5.2-4" stroke="var(--gold)" stroke-width="1" fill="none"/></svg>
        <span>kelumpangresort@mailnest.example</span>
      </li>
    </ul>

    <svg class="card-wave" viewBox="0 0 980 110" preserveAspectRatio="none" aria-hidden="true">
      <path d="M0 90 C 260 110, 560 100, 980 30 L 980 110 L 0 110 Z" fill="var(--ivory)"/>
      <path d="M0 102 C 300 112, 620 100, 980 55 L 980 110 L 0 110 Z" fill="var(--tan)"/>
    </svg>
  </main>
</body>
</html>
```